Lumo4Kart - a fintech company - business card

We need a business card design for our Payments Technology company in Sydney, Australia. We provide business with payment solutions expanding across EFTPOS machines, online payment gateways and mobile payment solutions. We would like to see designs that are clean, classy and professional.
Target Market(s)
Business professionals, executives, c-suite
Industry/Entity Type
Fintech
Contact Information for Business Card
Will be on 400gsm. Logo will most likely be spot gloss unless designer recommends otherwise.
Font styles to use
Sans Serif
Requirements
Must have
- We need our website (lumo4kart.com.au), email (contact@lumo4kart.com.au), mobile (0432 587 904) and direct phone number (02 6815 3927) to feature on the card along with our logo (attached) and the words "EFTPOS | ONLINE | MOBILE"
- Font = Roboto

```html
<!DOCTYPE html>
<html lang="en">
<head>
<meta charset="utf-8">
<title>Lumo4Kart business card</title>
<link href="https://fonts.googleapis.com/css2?family=Roboto:wght@400;500;700;900&display=swap" rel="stylesheet">
<style>
  :root {
    --backdrop: #d9d9d9;
    --card-white: #fdfdfd;
    --card-dark: #5f6062;
    --brand-blue: #2f6ea8;
    --name-blue: #1f4f86;
    --text-grey: #5a5c60;
    --tag-grey: #3e4044;
    --watermark: #e6e9ee;
    --shade: rgba(0,0,0,0.18);
  }
  * { margin: 0; padding: 0; box-sizing: border-box; }
  html, body {
    width: 1200px; height: 675px; overflow: hidden;
    background: var(--backdrop);
    font-family: "Roboto", sans-serif;
  }
  .canvas {
    position: relative; width: 1200px; height: 675px;
    display: flex; align-items: center; justify-content: center; gap: 60px;
  }
  .card {
    position: relative; width: 490px; height: 280px;
    border-radius: 18px; overflow: hidden;
    box-shadow: 0 10px 24px var(--shade);
  }
  .card-front { background: var(--card-white); }
  .front-watermark {
    position: absolute; left: 238px; top: 40px;
    width: 210px; height: 210px; border-radius: 50%;
    background: var(--watermark);
  }
  .holder {
    position: absolute; left: 60px; top: 96px; text-align: right; width: 150px;
  }
  .holder-name {
    color: var(--name-blue); font-weight: 500; font-size: 17px; letter-spacing: 1px;
  }
  .holder-role { color: var(--text-grey); font-size: 12px; margin-top: 1px; }
  .contact-list {
    position: absolute; left: 232px; top: 86px; list-style: none;
  }
  .contact-list li {
    display: flex; align-items: center; gap: 10px;
    color: var(--text-grey); font-size: 14px; line-height: 19px;
  }
  .contact-list svg { width: 12px; height: 12px; fill: var(--brand-blue); flex: none; }
  .services {
    position: absolute; left: 0; right: 0; bottom: 34px; text-align: center;
    color: var(--tag-grey); font-weight: 500; font-size: 13px; letter-spacing: 1.6px;
  }
  .card-back {
    background: linear-gradient(150deg, #6a6b6d 0%, var(--card-dark) 60%, #58595b 100%);
    display: flex; align-items: center; justify-content: center; gap: 18px;
  }
  .back-mark { width: 58px; height: 58px; border-radius: 50%; background: var(--brand-blue); }
  .back-name {
    color: #ffffff; font-weight: 900; font-size: 40px; letter-spacing: 1px;
  }
</style>
</head>
<body>
<main class="canvas">
  <section class="card card-front" aria-label="Card front">
    <div class="front-watermark" aria-hidden="true"></div>
    <div class="holder">
      <p class="holder-name">MARA ELLISON</p>
      <p class="holder-role">Manager</p>
    </div>
    <ul class="contact-list">
      <li><svg viewBox="0 0 24 24" aria-hidden="true"><path d="M6.6 10.8a15 15 0 0 0 6.6 6.6l2.2-2.2a1 1 0 0 1 1-.25 11.4 11.4 0 0 0 3.6.57 1 1 0 0 1 1 1V20a1 1 0 0 1-1 1A17 17 0 0 1 3 4a1 1 0 0 1 1-1h3.5a1 1 0 0 1 1 1c0 1.25.2 2.45.57 3.57a1 1 0 0 1-.25 1z"/></svg>02 6815 3927</li>
      <li><svg viewBox="0 0 24 24" aria-hidden="true"><path d="M7 1h10a2 2 0 0 1 2 2v18a2 2 0 0 1-2 2H7a2 2 0 0 1-2-2V3a2 2 0 0 1 2-2zm0 3v15h10V4zm5 16.2a1 1 0 1 0 0 .1z"/></svg>0432 587 904</li>
      <li><svg viewBox="0 0 24 24" aria-hidden="true"><path d="M2 5h20v14H2zm2 2v.5l8 5 8-5V7zm0 2.8V17h16V9.8l-8 5z"/></svg>contact@lumo4kart.com.au</li>
      <li><svg viewBox="0 0 24 24" aria-hidden="true"><path d="M12 2a10 10 0 1 0 0 20 10 10 0 0 0 0-20zm6.9 6h-2.9a15 15 0 0 0-1.4-3.6A8 8 0 0 1 18.9 8zM12 4c.8 1.2 1.5 2.5 1.9 4h-3.8c.4-1.5 1.1-2.8 1.9-4zM4.3 14a8 8 0 0 1 0-4h3.4a16 16 0 0 0 0 4zm.8 2h2.9c.3 1.3.8 2.5 1.4 3.6A8 8 0 0 1 5.1 16zM8 8H5.1a8 8 0 0 1 4.3-3.6C8.8 5.5 8.3 6.7 8 8zm4 12c-.8-1.2-1.5-2.5-1.9-4h3.8c-.4 1.5-1.1 2.8-1.9 4zm2.3-6H9.7a14 14 0 0 1 0-4h4.6a14 14 0 0 1 0 4zm.3 5.6c.6-1.1 1.1-2.3 1.4-3.6h2.9a8 8 0 0 1-4.3 3.6zm1.7-5.6a16 16 0 0 0 0-4h3.4a8 8 0 0 1 0 4z"/></svg>lumo4kart.com.au</li>
    </ul>
    <p class="services">EFTPOS | ONLINE | MOBILE</p>
  </section>

  <section class="card card-back" aria-label="Card back">
    <span class="back-mark" aria-hidden="true"></span>
    <span class="back-name">LUMO4KART</span>
  </section>
</main>
</body>
</html>
```